Investor Pitch Deck for Startup

We need a pitch deck to help us secure early funding for our new startup that will be active in the social media space. We have drafted out a 19 slide presentation, and have some other materials to help you prepare what we need.

We need to illustrate the pitch and make it visual, intuitive, and memorable. We are offering an abstract service, not a physical product - this might make it easier or harder to illustrate!

All materials will be provided after an NDA is signed.

Target Market(s)

This is aimed at angel investors.

Industry/Entity Type

Media

Font styles to use
Serif
Sans Serif

Requirements
Must have
• We are open to your suggestions about presentation and style.

```html
<!DOCTYPE html>
<html lang="en">
<head>
<meta charset="utf-8">
<title>Pitch Deck Template</title>
<link href="https://fonts.googleapis.com/css2?family=Figtree:wght@400;600;700;800&display=swap" rel="stylesheet">
<style>
:root{
  --red:#d0021b;
  --red-dark:#a8001a;
  --ink:#3c3c3c;
  --text:#2b2b2b;
  --rule:#9a9a9a;
  --bg:#000;
  --paper-top:#ffffff;
  --paper-bottom:#e6e6e6;
  --grey-head:#b8b8b8;
  --grey-cat:#d2d2d2;
  --row-a:#ffffff;
  --row-b:#efefef;
  --red-b:#dc3045;
  --dark-a:#4a4a4a;
  --dark-b:#6a6a6a;
}
*{margin:0;padding:0;box-sizing:border-box}
html,body{width:1061px;height:1200px;overflow:hidden;background:var(--bg)}
body{font-family:"Figtree",Arial,sans-serif;color:var(--text);position:relative}
.slide{position:absolute;width:520px;height:390px;overflow:hidden;
  background:linear-gradient(180deg,var(--paper-top) 0%,var(--paper-bottom) 100%)}
.slide::before{content:"";position:absolute;left:0;top:0;right:0;height:9px;background:var(--red)}
.s1{left:8px;top:8px}.s2{left:535px;top:8px}
.s3{left:8px;top:405px}.s4{left:535px;top:405px}
.s5{left:8px;top:802px}.s6{left:535px;top:802px}
.red{color:var(--red)}
.heading{position:absolute;left:22px;top:18px;font-size:29px;font-weight:700;color:var(--ink);line-height:36px}
.heading::before{content:"";position:absolute;left:-22px;top:8px;width:12px;height:20px;background:var(--red)}
.footer{position:absolute;left:14px;right:14px;top:355px;border-top:1px solid var(--rule);height:35px}
.footer .logo{position:absolute;left:8px;top:5px;font-size:21px;font-weight:800;color:var(--red)}
.footer .nav{position:absolute;right:30px;top:7px;display:flex;gap:4px}
.nav span{width:22px;height:20px;background:var(--red);border-radius:3px;display:block}
.nav svg{display:block}
.footer .page{position:absolute;right:0;top:6px;padding-left:10px;border-left:1px solid var(--rule);font-size:13px;color:var(--ink);line-height:22px}
.band{position:absolute;left:0;right:0;bottom:0;background:linear-gradient(180deg,var(--red) 0%,var(--red-dark) 100%)}
.rule{position:absolute;height:1px;background:var(--rule)}
/* title */
.s1 .rule{left:44px;right:44px}
.title{position:absolute;left:0;right:0;top:82px;text-align:center;font-size:50px;font-weight:800;line-height:56px;color:var(--ink)}
.subtitle{position:absolute;left:0;right:0;top:142px;text-align:center;font-size:40px;font-weight:400;line-height:46px;color:var(--ink)}
.s1 .big-logo{position:absolute;left:42px;top:243px;font-size:33px;font-weight:800;color:var(--red)}
.byline{position:absolute;right:44px;top:243px;text-align:right;font-size:13px;line-height:17px;color:var(--ink)}
.byline strong{display:block;color:var(--red);font-size:15px;font-weight:700}
/* about */
.about{position:absolute;left:22px;right:18px;top:70px;font-size:14.5px;line-height:19.5px;text-align:justify;color:var(--text)}
.about p{margin-bottom:12px}
.about b{color:var(--red);font-weight:700}
/* services */
.services{position:absolute;left:42px;top:83px;list-style:none}
.services li{font-size:18.5px;line-height:25px;color:var(--ink);padding-left:20px;position:relative}
.services li::before{content:"";position:absolute;left:1px;top:9px;width:7px;height:7px;background:var(--red);transform:rotate(45deg)}
.team-photo{position:absolute;left:226px;top:77px;width:266px;height:240px;border-radius:6px;
  background:radial-gradient(ellipse at 50% 55%,#4a4a52 0%,#6b6b73 40%,rgba(230,230,230,0) 72%)}
/* table */
.grid{position:absolute;left:24px;top:73px;width:471px;border-collapse:collapse;font-size:9.5px}
.grid th{height:25px;font-size:13px;font-weight:700;text-align:center}
.grid th.cat{background:var(--grey-head);color:var(--ink);width:234px}
.grid th.o1{background:var(--red);color:#fff;width:117px}
.grid th.o2{background:var(--dark-a);color:#fff}
.grid td{height:18px;padding:0}
.grid tr.group td{background:var(--grey-cat);font-weight:700;font-size:10px;padding-left:6px;color:var(--text)}
.grid td.item{padding-left:30px;color:var(--text)}
.grid td.yes,.grid td.no{text-align:center;color:#fff}
.grid tr.a td.item{background:var(--row-a)}.grid tr.b td.item{background:var(--row-b)}
.grid tr.a td.yes{background:var(--red)}.grid tr.b td.yes{background:var(--red-b)}
.grid tr.a td.no{background:var(--dark-a)}.grid tr.b td.no{background:var(--dark-b)}
.grid tr.group td.blank{background:var(--grey-cat)}
/* contact */
.map{position:absolute;left:32px;top:74px;width:222px;height:218px;border:4px solid #fff;box-shadow:0 0 2px rgba(0,0,0,.35);
  background:linear-gradient(160deg,#d6e2b8 0%,#e3dfb8 40%,#b9d3e3 70%,#9fc6e0 100%)}
.contact{position:absolute;left:267px;top:72px;width:240px;font-size:9.5px;line-height:11.5px;color:var(--ink)}
.contact .lead{text-align:justify;margin-bottom:8px}
.contact .lead b{color:var(--red)}
.contact h4{color:var(--red);font-size:11px;font-weight:700;line-height:14px;margin-top:3px}
.social{position:absolute;left:34px;top:318px;display:flex;align-items:center;gap:6px;font-size:11.5px;color:var(--ink)}
.social span{width:18px;height:18px;background:var(--red);border-radius:3px;display:block}
.social em{font-style:normal;margin-left:2px}
.social em b{color:var(--red);font-weight:700}
/* thanks */
.s6 .rule{left:44px;right:44px}
.thanks{position:absolute;left:0;right:0;top:100px;text-align:center;font-size:68px;font-weight:800;letter-spacing:-1px;line-height:80px;color:var(--ink)}
.s6 .big-logo{position:absolute;left:0;right:0;top:235px;text-align:center;font-size:33px;font-weight:800;color:var(--red)}
</style>
</head>
<body>

<section class="slide s1">
  <div class="rule" style="top:53px"></div>
  <h1 class="title"><span class="red">TITLE</span> PROJECT</h1>
  <p class="subtitle">subtext <span class="red">presentation</span></p>
  <div class="rule" style="top:221px"></div>
  <div class="big-logo">LOGO</div>
  <div class="byline">Presentation by<strong>Clara Wendt</strong></div>
  <div class="band" style="height:90px">
    <svg width="520" height="90" viewBox="0 0 520 90"><polygon points="258,22 284,44 258,70 258,54 268,44 258,34" fill="#fff"/></svg>
  </div>
</section>

<section class="slide s2">
  <h2 class="heading"><span class="red">About</span> Company</h2>
  <div class="about">
    <p><b>Lorem ipsum</b> dolor sit amet, consectetuer adipiscing elit. Maecenas porttitor congue massa. Fusce posuere, magna sed pulvinar ultricies, purus lectus malesuada libero, sit amet commodo magna eros quis urna.</p>
    <p><b>Nunc viverra imperdiet enim</b>. Fusce est. Vivamus a tellus. Pellentesque habitant morbi tristique senectus et netus et malesuada fames ac turpis egestas. Proin pharetra nonummy pede. Mauris et orci.</p>
    <p><b>Aenean nec lorem</b>. In porttitor. Donec laoreet nonummy augue.</p>
    <p>Suspendisse dui purus, scelerisque at, vulputate vitae, pretium mattis, nunc. Mauris eget neque at sem venenatis eleifend. Ut nonummy.</p>
    <p><b>Fusce aliquet pede non pede</b>.<br>Suspendisse dapibus lorem pellentesque magna. Integer nulla.</p>
  </div>
  <div class="footer"><span class="logo">LOGO</span>
    <div class="nav"><span><svg width="22" height="20"><polyline points="13,5 8,10 13,15" fill="none" stroke="#fff" stroke-width="3"/></svg></span><span><svg width="22" height="20"><polyline points="9,5 14,10 9,15" fill="none" stroke="#fff" stroke-width="3"/></svg></span></div>
    <span class="page">2</span></div>
</section>

<section class="slide s3">
  <h2 class="heading"><span class="red">Our</span> Services</h2>
  <ul class="services">
    <li>Lorem ipsum</li><li>Lorem ipsum</li><li>Lorem ipsum</li><li>Lorem ipsum</li><li>Lorem ipsum</li>
    <li>Lorem ipsum</li><li>Lorem ipsum</li><li>Lorem ipsum</li><li>Lorem ipsum</li><li>Lorem ipsum</li>
  </ul>
  <div class="team-photo" role="img" aria-label="Photo of a business team standing together in dark suits"></div>
  <div class="footer"><span class="logo">LOGO</span>
    <div class="nav"><span><svg width="22" height="20"><polyline points="13,5 8,10 13,15" fill="none" stroke="#fff" stroke-width="3"/></svg></span><span><svg width="22" height="20"><polyline points="9,5 14,10 9,15" fill="none" stroke="#fff" stroke-width="3"/></svg></span></div>
    <span class="page">3</span></div>
</section>

<section class="slide s4">
  <h2 class="heading"><span class="red">Table</span> Presentation</h2>
  <table class="grid">
    <tr><th class="cat">CATEGORY</th><th class="o1">OPTION 1</th><th class="o2">OPTION 2</th></tr>
    <tr class="group"><td>Category 1</td><td class="blank"></td><td class="blank"></td></tr>
    <tr class="a"><td class="item">Lorem ipsum dolor sit amet</td><td class="yes">Yes</td><td class="no">-</td></tr>
    <tr class="b"><td class="item">Lorem ipsum dolor sit amet</td><td class="yes">Yes</td><td class="no">-</td></tr>
    <tr class="a"><td class="item">Lorem ipsum dolor sit amet</td><td class="yes">Yes</td><td class="no">-</td></tr>
    <tr class="group"><td>Category 2</td><td class="blank"></td><td class="blank"></td></tr>
    <tr class="a"><td class="item">Lorem ipsum dolor sit amet</td><td class="yes">Yes</td><td class="no">-</td></tr>
    <tr class="b"><td class="item">Lorem ipsum dolor sit amet</td><td class="yes">Yes</td><td class="no">-</td></tr>
    <tr class="a"><td class="item">Lorem ipsum dolor sit amet</td><td class="yes">Yes</td><td class="no">-</td></tr>
    <tr class="b"><td class="item">Lorem ipsum dolor sit amet</td><td class="yes">Yes</td><td class="no">-</td></tr>
    <tr class="group"><td>Category 3</td><td class="blank"></td><td class="blank"></td></tr>
    <tr class="a"><td class="item">Lorem ipsum dolor sit amet</td><td class="yes">Yes</td><td class="no">-</td></tr>
    <tr class="b"><td class="item">Lorem ipsum dolor sit amet</td><td class="yes">Yes</td><td class="no">-</td></tr>
  </table>
  <div class="footer"><span class="logo">LOGO</span>
    <div class="nav"><span><svg width="22" height="20"><polyline points="13,5 8,10 13,15" fill="none" stroke="#fff" stroke-width="3"/></svg></span><span><svg width="22" height="20"><polyline points="9,5 14,10 9,15" fill="none" stroke="#fff" stroke-width="3"/></svg></span></div>
    <span class="page">4</span></div>
</section>

<section class="slide s5">
  <h2 class="heading"><span class="red">Contact</span> Info</h2>
  <div class="map" role="img" aria-label="Regional map showing the office location"></div>
  <div class="contact">
    <p class="lead"><b>Lorem ipsum</b> dolor sit amet, consectetuer adipiscing elit. Maecenas porttitor congue massa. Fusce posuere, magna sed pulvinar ultricies, purus lectus malesuada libero, sit amet commodo magna eros quis urna.</p>
    <h4>Address</h4><p>48 Lindenfield Road<br>Harrowgate<br>20417</p>
    <h4>Phone</h4><p>0400-218-635</p>
    <h4>FAX</h4><p>0400-218-636</p>
    <h4>Email</h4><p>hello@northpier.co</p>
    <h4>Website</h4><p>www.northpier.co</p>
  </div>
  <div class="social"><span></span><span></span><span></span><span></span><em>@NORTH<b>PIER</b></em></div>
  <div class="footer"><span class="logo">LOGO</span>
    <div class="nav"><span><svg width="22" height="20"><polyline points="13,5 8,10 13,15" fill="none" stroke="#fff" stroke-width="3"/></svg></span><span><svg width="22" height="20"><polyline points="9,5 14,10 9,15" fill="none" stroke="#fff" stroke-width="3"/></svg></span></div>
    <span class="page">5</span></div>
</section>

<section class="slide s6">
  <div class="rule" style="top:66px"></div>
  <h2 class="thanks"><span class="red">Thank</span>You</h2>
  <div class="rule" style="top:208px"></div>
  <div class="big-logo">LOGO</div>
  <div class="band" style="height:89px"></div>
</section>

</body>
</html>
```